Trading company needs a non alcoholic beer Can design

We KLM are trading company , food Distributors in Africa -RD Congo/Kinshasa .We want to do a Private label non alcoholic beer 500ml can and need a design for this Project .
the Brand Name is : NUVA BREW
We want it to be similar NOT a copy of Velmora 0.0% can ( picture
attached ) as we want to respect the intellectual properties .so we prefer to use the same colors but more elegant ,modern style .
thanks.
THE DESIGN MUST STATE ITS A NON ALCOHOLIC BEER
PLZ SEARCH FOR VELMORA 0.0% MALT DRINK YOU WILL FIND 2 DESIGNS OLD AND NEW WE NEED SOMTHING SIMILAR TO THESE DESIGNS ,KINDLY USE SAME COLORS AND THE 0.0% SHOULD BE IN THE MIDDLE OF THE CAN .
Target Market(s)
THE PRODUCT WILL BE SOLD IN THE SUPERMASRKTS / MODERN TRADE

```html
<!DOCTYPE html>
<html lang="en">
<head>
<meta charset="utf-8">
<title>NUVA BREW Non Alcoholic Beer – Can Label</title>
<link href="https://fonts.googleapis.com/css2?family=Roboto+Slab:wght@800;900&family=Lilita+One&display=swap" rel="stylesheet">
<style>
  :root {
    --page: #eceef1;
    --silver-dark: #9ea3a9;
    --silver-mid: #d4d7db;
    --silver-light: #f4f5f6;
    --red: #d8321f;
    --red-deep: #b8200f;
    --red-light: #ec5a3c;
    --blue: #1f4fa0;
    --blue-deep: #173a7c;
    --white: #fbfaf6;
    --gold: #f3c545;
    --gold-deep: #d9a52a;
  }
  * { margin: 0; padding: 0; box-sizing: border-box; }
  html, body { width: 900px; height: 1200px; overflow: hidden; background: var(--page); }
  .label {
    position: relative;
    width: 900px; height: 1200px;
    background: linear-gradient(90deg, var(--silver-dark) 0%, var(--silver-mid) 18%, var(--silver-light) 40%, var(--silver-mid) 65%, var(--silver-light) 82%, var(--silver-dark) 100%);
    overflow: hidden;
  }
  .label-shapes { position: absolute; inset: 0; }
  .brand {
    position: absolute; left: 0; right: 0; top: 190px;
    display: flex; flex-direction: column; align-items: center;
    font-family: "Roboto Slab", serif; font-weight: 900;
    color: var(--white); line-height: 0.95; text-align: center;
  }
  .brand-top { font-size: 118px; letter-spacing: 2px; }
  .brand-bottom { font-size: 150px; letter-spacing: 2px; }
  .brand-dot {
    width: 22px; height: 22px; border-radius: 50%;
    background: var(--white); margin-bottom: 22px;
  }
  .product-type {
    position: absolute; left: 0; right: 0; top: 535px;
    font-family: "Roboto Slab", serif; font-weight: 800;
    color: var(--white); text-align: center;
    font-size: 40px; line-height: 1.05; letter-spacing: 1px;
  }
  .abv {
    position: absolute; left: 0; right: 0; top: 640px;
    display: flex; justify-content: center; align-items: flex-end;
    font-family: "Lilita One", sans-serif; color: var(--blue);
    -webkit-text-stroke: 10px var(--white); paint-order: stroke fill;
  }
  .abv-value { font-size: 200px; line-height: 0.9; font-style: italic; }
  .abv-side { display: flex; flex-direction: column; margin-left: 8px; margin-bottom: 12px; }
  .abv-percent { font-size: 90px; line-height: 0.9; }
  .abv-unit { font-size: 64px; line-height: 0.9; }
  .variant {
    position: absolute; left: 0; right: 0; top: 880px;
    font-family: "Roboto Slab", serif; font-weight: 900;
    color: var(--gold); text-align: center; line-height: 1;
  }
  .variant-small { font-size: 38px; letter-spacing: 3px; }
  .variant-large { font-size: 74px; letter-spacing: 2px; }
  .grain-art {
    position: absolute; left: 300px; top: 1010px;
    width: 300px; height: 120px; border-radius: 10px;
    background: radial-gradient(ellipse at center, rgba(243,197,69,0.55), rgba(217,165,42,0.15) 70%, transparent);
  }
</style>
</head>
<body>
<main class="label">
  <svg class="label-shapes" width="900" height="1200" viewBox="0 0 900 1200" aria-hidden="true">
    <defs>
      <linearGradient id="redBand" x1="0" y1="0" x2="1" y2="0">
        <stop offset="0" stop-color="var(--red-deep)"/>
        <stop offset="0.45" stop-color="var(--red-light)"/>
        <stop offset="1" stop-color="var(--red-deep)"/>
      </linearGradient>
    </defs>
    <path class="top-band" d="M170 0 H730 V560 L450 650 L170 560 Z" fill="url(#redBand)"/>
    <path class="variant-shield" d="M200 850 Q450 800 700 850 V1070 L450 1170 L200 1070 Z" fill="url(#redBand)"/>
  </svg>

  <div class="brand">
    <span class="brand-dot"></span>
    <span class="brand-top">NUVA</span>
    <span class="brand-bottom">BREW</span>
  </div>

  <p class="product-type">NON ALCOHOLIC<br>BEER</p>

  <div class="abv">
    <span class="abv-value">0.0</span>
    <span class="abv-side">
      <span class="abv-percent">%</span>
      <span class="abv-unit">ALC.</span>
    </span>
  </div>

  <div class="variant">
    <div class="variant-small">PREMIUM</div>
    <div class="variant-large">ORIGINAL</div>
  </div>

  <div class="grain-art" role="img" aria-label="Line illustration of wheat ears and a sack of barley grain"></div>
</main>
</body>
</html>
```